I need a letterhead for a newsletter that will go out quarterly to the dentists of the 18th district. It is called "The Quarterly Ledger" We are in Amarillo TX and have this landmark in the photo as our most prominent feature. If it could be used, that would be cool.
This is a professional organization newsletter so the letterhead should be somewhat professional.

Target Market(s)

Dentists

Industry/Entity Type

Dental

Font styles to use
Serif

Colors

Designer to choose only greyscale colors for use in the design.

Requirements
Must have
• I want the title of "The Quarterly Ledger" to be the on top with the phrase "Brookvale Regional Dental Guild" written underneath.
Nice to have
• the photo incorporated could be incorporated in black and white or color along the bottom of the letterhead or with the title inside the photo.
Should not have
• I don't want it to be cartoony. I want it to be stylish and elegant and professional.

```html
<!DOCTYPE html>
<html lang="en">
<head>
<meta charset="utf-8">
<title>The Quarterly Ledger – Letterhead</title>
<link href="https://fonts.googleapis.com/css2?family=Bitter:wght@800&family=Lato:wght@400;700&family=Open+Sans:wght@400;600&display=swap" rel="stylesheet">
<style>
  :root {
    --backdrop: #e4e5e6;
    --paper: #ffffff;
    --title-blue: #2a5596;
    --ink: #2b2b2b;
    --body-ink: #4a4a4a;
    --footer-dark: #1f2a30;
    --footer-text: #ffffff;
    --rule: #6c767c;
  }
  html, body {
    margin: 0;
    width: 1040px;
    height: 1200px;
    overflow: hidden;
    background: var(--backdrop);
  }
  .letterhead {
    position: absolute;
    left: 54px;
    top: 0;
    width: 931px;
    height: 1200px;
    background: var(--paper);
    overflow: hidden;
    font-family: "Open Sans", sans-serif;
    color: var(--body-ink);
  }
  .masthead {
    position: absolute;
    top: 40px;
    left: 0;
    width: 100%;
    text-align: center;
  }
  .masthead__title {
    margin: 0;
    font-family: "Bitter", serif;
    font-weight: 800;
    font-size: 35px;
    line-height: 1;
    letter-spacing: 0.5px;
    color: var(--title-blue);
    text-transform: uppercase;
  }
  .masthead__subtitle {
    margin: 4px 0 0;
    font-family: "Lato", sans-serif;
    font-size: 17px;
    letter-spacing: 1.2px;
    color: var(--ink);
    text-transform: uppercase;
  }
  .letter {
    position: absolute;
    left: 87px;
    top: 248px;
    width: 753px;
    font-size: 14.5px;
  }
  .letter p { margin: 0; }
  .letter__date { margin-bottom: 18px !important; }
  .letter__recipient { line-height: 17.5px; }
  .letter__greeting { margin-top: 46px !important; }
  .letter__body p {
    margin-top: 27px;
    line-height: 27px;
    text-align: justify;
    hyphens: auto;
  }
  .letter__closing { margin-top: 55px !important; }
  .signature__name {
    margin-top: 60px !important;
    font-size: 18px;
    font-weight: 600;
    color: var(--ink);
  }
  .signature__role { margin-top: 4px !important; }
  .footer-band {
    position: absolute;
    left: 0;
    bottom: 0;
    width: 931px;
    height: 200px;
  }
  .footer-contact {
    position: absolute;
    left: 71px;
    top: 1114px;
    width: 553px;
    font-family: "Lato", sans-serif;
    font-size: 17px;
    color: var(--footer-text);
    white-space: nowrap;
  }
  .footer-contact__address {
    padding-bottom: 8px;
    border-bottom: 1px solid var(--rule);
  }
  .footer-contact__lines { margin-top: 8px; }
  .footer-contact b { font-weight: 700; }
</style>
</head>
<body>
<main class="letterhead">
  <header class="masthead">
    <h1 class="masthead__title">The Quarterly Ledger</h1>
    <p class="masthead__subtitle">Brookvale Regional Dental Guild</p>
  </header>

  <section class="letter">
    <p class="letter__date">Issuing Date: May 5, 2018</p>
    <div class="letter__recipient">
      <p>Name Of Employee Mr. XYZABC</p>
      <p>Address of Employee</p>
      <p>Address Line 2 etc..</p>
    </div>
    <p class="letter__greeting">Dear Mr.XYZABC</p>
    <div class="letter__body">
      <p>Lorem Ipsum has been the industry's standard dummy text ever since the 1500s, when an unknown printer took a galley of type and scrambled it to make a type specimen book. It has survived not only five centuries, but also the leap into electronic typesetting, remaining essentially unchanged. It was popularised in the 1960s with the release of Pressmark sheets containing Lorem Ipsum passages, and more recently with desktop publishing software like Quillset Layout including versions of Lorem Ipsum.</p>
      <p>Lorem Ipsum is simply dummy text of the printing and typesetting industry. Lorem Ipsum has been the industry's standard dummy text ever since the 1500s, when an unknown printer took a galley of type and scrambled it to make a type specimen book.</p>
      <p>It has survived not only five centuries, but also the leap into electronic typesetting, remaining essentially unchanged. It was popularised in the 1960s with the release of Pressmark sheets containing Lorem IpsumIpsum passages.</p>
    </div>
    <p class="letter__closing">Yours Sincerely</p>
    <p class="signature__name">Marian Ellsworth</p>
    <p class="signature__role">Managing Director</p>
  </section>

  <svg class="footer-band" viewBox="0 0 931 200">
    <defs>
      <clipPath id="wave-clip">
        <path d="M0,89 L406,89 C560,62 720,2 931,5 L931,200 L0,200 Z"/>
      </clipPath>
      <linearGradient id="landmark-tones" x1="0" y1="0" x2="0" y2="1">
        <stop offset="0" stop-color="#233656"/>
        <stop offset="0.45" stop-color="#4d5a6a"/>
        <stop offset="0.75" stop-color="#7a4532"/>
        <stop offset="1" stop-color="#9a5a3e"/>
      </linearGradient>
      <linearGradient id="landmark-fade" x1="0" y1="0" x2="1" y2="0">
        <stop offset="0" stop-color="#1f2a30" stop-opacity="1"/>
        <stop offset="0.35" stop-color="#1f2a30" stop-opacity="0"/>
      </linearGradient>
    </defs>
    <g clip-path="url(#wave-clip)">
      <rect x="0" y="0" width="931" height="200" fill="var(--footer-dark)"/>
      <rect role="img" aria-label="Photograph of the canyon rock landmark under a blue sky" x="624" y="0" width="307" height="200" fill="url(#landmark-tones)"/>
      <rect x="624" y="0" width="307" height="200" fill="url(#landmark-fade)"/>
    </g>
  </svg>

  <div class="footer-contact">
    <div class="footer-contact__address">218 Canyon Ridge Road,&nbsp; 79104 Brookvale</div>
    <div class="footer-contact__lines"><b>P:</b> 044-387 210 654 | <b>E:</b> info@qledger.org | <b>www.qledger.org</b></div>
  </div>
</main>
</body>
</html>
```